International Petrochemical business needs a web design for Clearway Desk system

We need a web design for a "Clearway Desk" system for an international petrochemical company. The web site is used internally within the company. It is hosted by an internal department which provides government permit request service for other departments.

We would like to see designs of two pages using color light blue. (home page, internal page as attached).
Home Page:
1. Header has a background image and small animation. Header on home page can be taller than the header of the internal page.
2. Layout as attached.

Internal Page:
1. Header can use the same background image as the home page and can be shorter to utilize the page for content.
2. The blue icon behind every captions represent an icon. When user move mouse over this icon, it displays the caption in Thai language as a tooltip. This icon needs to be redesign.

The final design should communicate the followings:
- Excellent service provided system in terms of time and accurary
- Rapid growth of business via building petrochemical refinery plant

For Internal Page, the blue circle behind every captions represent an icon. When mouse over this icon, a tool tip showing the caption in Thai language is shown. Please also design this icon..

There are more feedbacks from customer as followed:

1. Banner should consists of 
    1.1 "Approved" stamp on paper
    1.2 An image of Garuda. It is used on every government documents in Thailand
    1.3 Image of petrochemical plant
2. Each menu item (Home, Permit, Search, etc) should have different colors. Drop down menu will use the same color as its parent menu item.
3. Overall tone of the web page should be light blue with background of the body the web page in white
4. "New Request" button should use green color with icon on it
5. Table header of each box in the body of the page should use dark blue background with text in white

Please kindly submit your revisions.
Thank you.

Reason: We get some late feedbacks from customers which was just updated to all designers.

• 1. Design for 1024x768 screen resolution
2. Use light blue theme
3. Background of header where the company logo is must have white background

```html
<!DOCTYPE html>
<html lang="en">
<head>
<meta charset="utf-8">
<title>Clearway Desk – Request Form</title>
<link href="https://fonts.googleapis.com/css2?family=Nunito+Sans:wght@400;600;700&display=swap" rel="stylesheet">
<style>
:root{
  --page:#ffffff;
  --panel:#eef5fb;
  --white:#ffffff;
  --line:#c9d9e6;
  --text:#555555;
  --muted:#9a9a9a;
  --label:#4a4a4a;
  --blue:#2a7fc1;
  --navy:#1d4f7c;
  --green:#3aa34a;
  --icon:#7fbde6;
  --dark:#5f5f5f;
  --req:#c0392b;
  --m-home:#2a7fc1;
  --m-permits:#3aa34a;
  --m-search:#e08a1e;
  --m-report:#8e5bb5;
  --m-admin:#d0453a;
  --m-help:#18a3a3;
}
*{box-sizing:border-box;margin:0;padding:0}
html,body{width:777px;height:1200px;overflow:hidden}
body{background:var(--page);font-family:"Nunito Sans",Arial,sans-serif;color:var(--text);position:relative}
.abs{position:absolute}
.hero{left:0;top:0;width:777px;height:84px;background:linear-gradient(180deg,#3b3452 0%,#a55a5a 45%,#d98a5a 62%,#3a3f4a 100%)}
.brand{left:44px;top:14px;width:113px;height:56px;background:var(--white);display:flex;align-items:center;justify-content:center;gap:5px;font-weight:700;font-size:10px;color:var(--blue)}
.brand i{width:10px;height:10px;border-radius:50%;background:var(--blue)}
.nav{left:44px;top:84px;width:692px;height:35px;background:var(--white);border:1px solid #d6d6d6;display:flex}
.nav a{display:flex;align-items:center;justify-content:center;font-size:11px;color:#444;text-decoration:none;border-right:1px solid #dedede;border-top:3px solid var(--c);height:100%}
.nav a.on{background:var(--c);color:var(--white)}
h1{left:41px;top:135px;font-size:21px;font-weight:400;color:#555}
.panel{left:42px;top:173px;width:692px;height:803px;background:var(--panel);border-bottom:2px solid #cddceb}
.lbl{width:190px;text-align:right;font-size:9px;font-weight:700;color:var(--label);letter-spacing:.2px;line-height:12px}
.lbl b{color:var(--req);margin-right:5px}
.ico{width:11px;height:9px}
.val{font-size:10px;color:var(--muted);line-height:12px}
.field{left:226px;width:176px;height:24px;background:var(--white);border:1px solid var(--line);font-size:10px;color:var(--muted);padding:6px 7px}
.area{left:226px;width:282px;height:80px;background:var(--white);border:1px solid var(--line);font-size:8px;color:var(--muted);padding:7px 7px;line-height:17px;overflow:hidden;white-space:nowrap}
.btn{color:var(--white);font-size:10px;display:flex;align-items:center;justify-content:center;gap:6px;font-weight:600;letter-spacing:.3px}
.tag{height:13px;border:1px solid #aaa;background:var(--white);font-size:8.5px;color:#666;display:flex;align-items:center;justify-content:space-between;padding:0 4px;white-space:nowrap}
.tag span{color:var(--req);font-weight:700;font-size:10px}
.tip{left:598px;top:158px;width:84px;height:34px;background:var(--white);border:1px solid #ccc;font-size:5.5px;line-height:8px;color:#555;padding:3px 6px}
.tbl{left:226px;top:702px;width:396px;height:169px;background:var(--white);border:1px solid var(--line)}
.thead{left:227px;top:703px;width:394px;height:24px;background:var(--navy)}
.th{font-size:7.5px;font-weight:700;color:var(--white);line-height:10px}
.td{font-size:10px;color:var(--muted)}
.td.link{color:var(--blue)}
.dot{width:6px;height:6px;border-radius:50%;background:#dcdcdc}
.fnav a{font-size:9px;color:#777;text-decoration:none}
.fcol{font-size:7.5px;color:#555;line-height:17px}
.rule{height:1px;background:#d4d4d4}
</style>
</head>
<body>
<div class="abs hero" role="img" aria-label="Petrochemical refinery plant at dusk"></div>
<div class="abs brand"><i></i>Norvale Chemical</div>
<nav class="abs nav">
  <a style="width:61px;--c:var(--m-home)">Home</a><a class="on" style="width:70px;--c:var(--m-permits)">Permits</a><a style="width:67px;--c:var(--m-search)">Search</a><a style="width:64px;--c:var(--m-report)">Report</a><a style="width:64px;--c:var(--m-admin)">Admin</a><a style="width:52px;--c:var(--m-help)">Help</a>
</nav>
<h1 class="abs">Request Form</h1>
<div class="abs panel"></div>

<svg width="0" height="0" style="position:absolute"><defs><symbol id="bubble" viewBox="0 0 11 9"><path d="M0 0h11v6H4L2 9V6H0z" fill="#7fbde6"/></symbol></defs></svg>

<div class="abs tip">Lorem ipsum dolor sit amet, consectetur adipiscing elit.</div>

<div class="abs lbl" style="left:0;top:198px">REQUEST DATE</div>
<div class="abs lbl" style="left:0;top:227px">REQUESTER NAME</div>
<div class="abs lbl" style="left:0;top:255px">CONTACT NO.</div>
<div class="abs lbl" style="left:0;top:283px"><b>•</b>COMPANY</div>
<div class="abs lbl" style="left:0;top:311px"><b>•</b>BRANCH</div>
<div class="abs lbl" style="left:0;top:340px"><b>•</b>DOCUMENT CATEGORY</div>
<div class="abs lbl" style="left:0;top:368px"><b>•</b>DOCUMENT TYPE</div>
<div class="abs lbl" style="left:0;top:396px"><b>•</b>EXPECTED USE DATE</div>
<div class="abs lbl" style="left:0;top:424px"><b>•</b>DETAIL</div>
<div class="abs lbl" style="left:0;top:509px">ATTACHEMENT</div>
<div class="abs lbl" style="left:0;top:566px"><b>•</b>COORDINATOR</div>
<div class="abs lbl" style="left:0;top:594px"><b>•</b>RELATED PERSON</div>
<div class="abs lbl" style="left:0;top:623px">REMARK</div>
<div class="abs lbl" style="left:0;top:707px">RELATED REQUEST</div>
<svg class="abs ico" style="left:195px;top:199px"><use href="#bubble"/></svg>
<svg class="abs ico" style="left:195px;top:228px"><use href="#bubble"/></svg>
<svg class="abs ico" style="left:195px;top:256px"><use href="#bubble"/></svg>
<svg class="abs ico" style="left:195px;top:284px"><use href="#bubble"/></svg>
<svg class="abs ico" style="left:195px;top:312px"><use href="#bubble"/></svg>
<svg class="abs ico" style="left:195px;top:341px"><use href="#bubble"/></svg>
<svg class="abs ico" style="left:195px;top:369px"><use href="#bubble"/></svg>
<svg class="abs ico" style="left:195px;top:397px"><use href="#bubble"/></svg>
<svg class="abs ico" style="left:195px;top:425px"><use href="#bubble"/></svg>
<svg class="abs ico" style="left:195px;top:510px"><use href="#bubble"/></svg>
<svg class="abs ico" style="left:195px;top:567px"><use href="#bubble"/></svg>
<svg class="abs ico" style="left:195px;top:595px"><use href="#bubble"/></svg>
<svg class="abs ico" style="left:195px;top:624px"><use href="#bubble"/></svg>
<svg class="abs ico" style="left:195px;top:708px"><use href="#bubble"/></svg>

<div class="abs lbl" style="left:403px;top:198px">REQUESTER EMPLOYEE NO</div>
<div class="abs lbl" style="left:403px;top:227px">TELEPHONE</div>
<svg class="abs ico" style="left:598px;top:199px"><use href="#bubble"/></svg>
<svg class="abs ico" style="left:598px;top:228px"><use href="#bubble"/></svg>
<div class="abs val" style="left:622px;top:198px;font-size:9px">xxxxxxxx</div>
<div class="abs val" style="left:622px;top:227px;font-size:9px">xxxx</div>

<div class="abs val" style="left:233px;top:198px">dd.mm.yyyy</div>
<div class="abs val" style="left:233px;top:227px">Alan Reyes</div>
<div class="abs field" style="top:249px;font-size:9px">xxx-xxx-xxxx</div>
<div class="abs field" style="top:277px">Please Select...</div>
<div class="abs field" style="top:305px">Please Select...</div>
<div class="abs field" style="top:334px">Please Select...</div>
<div class="abs field" style="top:362px">Please Select...</div>
<div class="abs field" style="top:390px">dd.mm.yyyy</div>
<div class="abs area" style="top:418px"><div>xxxxxxxxxxxxxxxxxxxxxxxxxxxxxxxx</div><div>xxxxxxxxxxxxxxxxxxxxxxxxxxxxxxxx</div></div>

<div class="abs field" style="top:503px;height:24px"></div>
<div class="abs btn" style="left:402px;top:503px;width:71px;height:24px;background:var(--dark)">BROWSE...</div>
<div class="abs btn" style="left:480px;top:503px;width:62px;height:24px;background:var(--blue)">ATTACH</div>
<div class="abs tag" style="left:227px;top:536px;width:70px">File1.docx<span>×</span></div>
<div class="abs tag" style="left:302px;top:536px;width:71px">File2.docx<span>×</span></div>

<div class="abs btn" style="left:226px;top:560px;width:42px;height:24px;background:var(--blue);font-size:11px">ADD</div>
<div class="abs tag" style="left:275px;top:565px;width:98px">Alan Reyes (HR)<span>×</span></div>
<div class="abs btn" style="left:226px;top:588px;width:42px;height:24px;background:var(--blue);font-size:11px">ADD</div>
<div class="abs tag" style="left:275px;top:593px;width:98px">Alan Reyes (IT)<span>×</span></div>
<div class="abs tag" style="left:382px;top:593px;width:126px">Dana Pruitt (Accounting)<span>×</span></div>
<div class="abs tag" style="left:516px;top:593px;width:110px">Ravi Holm (Finance)<span>×</span></div>

<div class="abs area" style="top:616px"><div>xxxxxxxxxxxxxxxxxxxxxxxxxxxxxxxx</div><div>xxxxxxxxxxxxxxxxxxxxxxxxxxxxxxxx</div></div>

<div class="abs tbl"></div>
<div class="abs thead"></div>
<div class="abs th" style="left:240px;top:710px">REQUEST NO.</div>
<div class="abs th" style="left:339px;top:710px">REQUEST DATE</div>
<div class="abs th" style="left:438px;top:710px">COMPANY</div>
<div class="abs th" style="left:551px;top:710px">BRANCH</div>

<div class="abs td link" style="left:240px;top:734px">yy-xxxx</div><div class="abs td" style="left:339px;top:734px">dd/mm/yyyy</div><div class="abs td" style="left:438px;top:734px">NVC</div><div class="abs td" style="left:551px;top:734px">GC1</div>
<div class="abs td link" style="left:240px;top:755px">yy-xxxx</div><div class="abs td" style="left:339px;top:755px">dd/mm/yyyy</div><div class="abs td" style="left:438px;top:755px">NVC</div><div class="abs td" style="left:551px;top:755px">GC2</div>
<div class="abs td link" style="left:240px;top:776px">yy-xxxx</div><div class="abs td" style="left:339px;top:776px">dd/mm/yyyy</div><div class="abs td" style="left:438px;top:776px">XYZ</div><div class="abs td" style="left:551px;top:776px">GC1</div>
<div class="abs td link" style="left:240px;top:797px">yy-xxxx</div><div class="abs td" style="left:339px;top:797px">dd/mm/yyyy</div><div class="abs td" style="left:438px;top:797px">XYZ</div><div class="abs td" style="left:551px;top:797px">GC2</div>
<div class="abs td link" style="left:240px;top:818px">yy-xxxx</div><div class="abs td" style="left:339px;top:818px">dd/mm/yyyy</div><div class="abs td" style="left:438px;top:818px">NVC</div><div class="abs td" style="left:551px;top:818px">GC2</div>
<div class="abs dot" style="left:558px;top:851px;background:var(--blue)"></div>
<div class="abs dot" style="left:572px;top:851px"></div>
<div class="abs dot" style="left:587px;top:851px"></div>
<div class="abs dot" style="left:601px;top:851px"></div>

<div class="abs btn" style="left:226px;top:898px;width:155px;height:36px;background:var(--green);font-size:10.5px">
  <svg width="11" height="11" viewBox="0 0 11 11"><path d="M5.5 1v9M1 5.5h9" stroke="#fff" stroke-width="2"/></svg>CREATE NEW REQUEST</div>
<div class="abs btn" style="left:395px;top:898px;width:64px;height:36px;background:var(--dark);font-size:11px">BACK</div>

<div class="abs fnav" style="left:236px;top:1000px"><a>Home</a></div>
<div class="abs fnav" style="left:290px;top:1000px"><a>Permits</a></div>
<div class="abs fnav" style="left:350px;top:1000px"><a>Search</a></div>
<div class="abs fnav" style="left:408px;top:1000px"><a>Report</a></div>
<div class="abs fnav" style="left:464px;top:1000px"><a>Admin</a></div>
<div class="abs fnav" style="left:519px;top:1000px"><a>Help</a></div>
<div class="abs rule" style="left:216px;top:1023px;width:346px"></div>

<div class="abs" style="left:58px;top:1062px;display:flex;align-items:center;gap:5px;font-size:10px;font-weight:700;color:#777"><i style="width:10px;height:10px;border-radius:50%;background:#888;display:block"></i>Norvale Chemical</div>
<div class="abs fcol" style="left:58px;top:1098px;width:150px;line-height:12px">Your about us information would fit here nicely.</div>
<div class="abs fcol" style="left:226px;top:1050px">Lorem ipsum dolor sit amet,<br>Aliquam tincidunt mauris<br>Lum auctor dapibus<br>Nunc dignissim risus id metus<br>Cras ornare tristique elit.</div>
<div class="abs fcol" style="left:396px;top:1050px">Lorem ipsum dolor sit amet,<br>Aliquam tincidunt mauris<br>Lum auctor dapibus<br>Nunc dignissim risus id metus<br>Cras ornare tristique elit.</div>
<div class="abs fcol" style="left:566px;top:1050px">Lorem ipsum dolor sit amet,<br>Aliquam tincidunt mauris<br>Lum auctor dapibus<br>Nunc dignissim risus id metus<br>Cras ornare tristique elit.</div>
<div class="abs rule" style="left:216px;top:1158px;width:346px"></div>
<div class="abs" style="left:0;width:777px;top:1169px;text-align:center;font-size:8px;color:#666">Copyright <b>NORVALE CHEMICAL</b> 2013. All rights reserved.</div>
</body>
</html>
```